One page design needed for a veteran owned brewery

I need a one page web designed for a brewery that is veteran owned. We give back a portion of our proceeds to veteran based nonprofit groups. halvardbrewing.example It is word press based.

Industry/Entity Type

Craft Brewery

Number of Pages Required

1 page

```html
<!DOCTYPE html>
<html lang="en">
<head>
<meta charset="utf-8">
<title>Halvard Brewery</title>
<link href="https://fonts.googleapis.com/css2?family=Montserrat:wght@300;400;600;800&family=Pathway+Gothic+One&display=swap" rel="stylesheet">
<style>
  :root {
    --ink: #111111;
    --charcoal: #3a3a3a;
    --white: #ffffff;
    --leaf: #9ab873;
    --leaf-deep: #7fa34e;
    --mist: #eeeeee;
  }
  * { margin: 0; padding: 0; box-sizing: border-box; }
  html, body { width: 1200px; height: 666px; overflow: hidden; background: var(--white); }
  .page { position: relative; width: 1200px; height: 666px; overflow: hidden; color: var(--ink); }

  .site-header { position: absolute; left: 0; top: 0; width: 1200px; height: 122px; }
  .brand-mark {
    position: absolute; left: 206px; top: 24px; width: 80px;
    display: flex; flex-direction: column; align-items: center; gap: 6px;
    font-family: "Montserrat", sans-serif; font-weight: 800;
    font-size: 13px; color: var(--charcoal); letter-spacing: 0.3px;
  }
  .brand-mark .dot { width: 44px; height: 44px; border-radius: 50%; background: var(--charcoal); }
  .site-title {
    position: absolute; left: 341px; top: 38px;
    font-family: "Montserrat", sans-serif; font-weight: 800;
    font-size: 48px; letter-spacing: 0; line-height: 1;
    color: var(--ink);
  }
  .find-more {
    position: absolute; left: 960px; top: 94px;
    font-family: "Montserrat", sans-serif; font-weight: 600;
    font-size: 10px; color: var(--leaf-deep); letter-spacing: 0.2px;
  }
  .header-rule { position: absolute; left: 0; top: 115px; width: 1200px; height: 6px; background: var(--ink); }

  .mission { position: absolute; left: 0; top: 121px; width: 1200px; height: 349px; }
  .mission-backdrop {
    position: absolute; left: 450px; top: 20px; width: 310px; height: 310px;
    border-radius: 50%; border: 8px solid var(--mist);
  }
  .mission-text {
    position: absolute; left: 307px; top: 70px; width: 640px;
    text-align: center;
    font-family: "Pathway Gothic One", sans-serif;
    font-size: 22px; line-height: 24px; color: var(--ink);
  }

  .quote-band { position: absolute; left: 0; top: 469px; width: 1200px; height: 144px; background: var(--leaf); color: var(--white); }
  .quote-band svg { position: absolute; }
  .quote {
    position: absolute; left: 340px; top: 22px; width: 576px;
    text-align: center; font-family: "Montserrat", sans-serif; font-weight: 300;
    font-size: 13px; line-height: 19px;
  }
  .attribution {
    position: absolute; right: 252px; top: 90px; text-align: right;
    font-family: "Montserrat", sans-serif; font-weight: 300;
    font-size: 12.5px; line-height: 18px;
  }
  .attribution strong { font-weight: 600; }
</style>
</head>
<body>
<div class="page">
  <header class="site-header">
    <div class="brand-mark"><span class="dot"></span>HALVARD</div>
    <h1 class="site-title">HALVARD BREWERY</h1>
    <a class="find-more">- FIND OUT MORE -</a>
    <div class="header-rule"></div>
  </header>

  <section class="mission">
    <div class="mission-backdrop" aria-hidden="true"></div>
    <p class="mission-text">
      WE ARE A VETERAN OWNED AND OPERATED BREWERY. OUR GOAL IS TO DONATE A PERCENTAGE OF OUR PROCEEDS TO VETERAN ORGANIZATIONS AND OUR LOCAL HEROES.<br>
      Halvard Brewery is a craft brewery in Millbrook, IN that will have a wide breadth of beers with a full kitchen.<br>
      We believe the transition from military life to civilian life can be a difficult road. We are trained by the military to be tough, battle harden soldiers ready for combat. However, the exit training is not nearly enough to fight the difference of civilian life &ndash; leaving some vets feeling left behind and causing many to take their own life.<br>
      The Halvard Brewery will work to change that!
    </p>
  </section>

  <section class="quote-band">
    <svg width="16" height="16" style="left:365px;top:14px" aria-hidden="true"><path d="M1.5 16V1.5H16" fill="none" stroke="#fff" stroke-width="3"/></svg>
    <svg width="16" height="16" style="left:858px;top:52px" aria-hidden="true"><path d="M0 14.5H14.5V0" fill="none" stroke="#fff" stroke-width="3"/></svg>
    <p class="quote">We are a veteran owned brewery, brewing for veterans and local heroes.<br>Coming to Millbrook in 2019.</p>
    <p class="attribution"><strong>Dale Hollis</strong>, Founder, Owner, Brewer<br>U.S. Army, 1987-1991</p>
  </section>
</div>
</body>
</html>
```